Bref créative
Hidden Meadows Stationary
Business Card, Letterhead, Envelope, Compliment Slip
Simple
Emre Karabulut
Mr
47 Foxglove Road,
Ilford,
Essex,
RM4 8TN
emre@hddnmdws.com
www.hddnmdws.com
Vat No: 472 8610 35
Vat No to be used in letterhead.
Logo, Maybe even a part of the logo....We're open to ideas.
HM Logo (If any other format is needed please let us know.

```html
<!DOCTYPE html>
<html lang="en">
<head>
<meta charset="utf-8">
<title>Hidden Meadows Stationary</title>
<link rel="stylesheet" href="https://fonts.googleapis.com/css2?family=Questrial&display=swap">
<style>
  :root {
    --backdrop: #c9c9c9;
    --paper: #ffffff;
    --paper-edge: #b9b9b9;
    --brand-green: #6cb33f;
    --ink: #3c3c3c;
    --ink-soft: #7a7a7a;
    --card-grey-light: #f4f4f4;
    --card-grey-dark: #cfcfcf;
  }
  * { margin: 0; padding: 0; box-sizing: border-box; }
  html, body { width: 1200px; height: 655px; overflow: hidden; }
  body {
    background: var(--backdrop);
    font-family: "Questrial", Arial, sans-serif;
    color: var(--ink);
    position: relative;
  }
  .sheet {
    position: absolute;
    background: var(--paper);
    box-shadow: 0 0 0 1px var(--paper-edge);
  }

  /* brand block */
  .brand { position: absolute; display: flex; align-items: flex-start; gap: 6px; }
  .brand__dot { border-radius: 50%; background: var(--brand-green); flex: none; }
  .brand__name { color: var(--brand-green); line-height: 0.92; letter-spacing: -0.5px; }
  .brand__tagline { color: var(--ink-soft); margin-top: 3px; letter-spacing: 0; }

  .web { position: absolute; color: var(--ink); }
  .contact { position: absolute; color: var(--ink); line-height: 1.55; }

  /* letterhead */
  .letterhead { left: 197px; top: 19px; width: 456px; height: 624px; }
  .letterhead .brand { left: 16px; top: 22px; }
  .letterhead .brand__dot { width: 14px; height: 14px; margin-top: 6px; }
  .letterhead .brand__name { font-size: 27px; }
  .letterhead .brand__tagline { font-size: 6px; }
  .letterhead .web { right: 18px; top: 20px; font-size: 7px; }
  .letterhead .contact { left: 16px; bottom: 26px; font-size: 6px; }

  /* business card back */
  .card-back {
    left: 29px; top: 283px; width: 154px; height: 77px;
    background: radial-gradient(ellipse at center, var(--card-grey-light) 0%, var(--card-grey-dark) 100%);
  }
  .card-back .brand { left: 50%; top: 14px; transform: translateX(-50%); }
  .card-back .brand__dot { width: 8px; height: 8px; margin-top: 3px; }
  .card-back .brand__name { font-size: 15px; }
  .card-back .brand__tagline { font-size: 4px; }
  .card-back .web { left: 0; right: 0; bottom: 6px; text-align: center; font-size: 4px; }

  /* business card front */
  .card-front { left: 29px; top: 367px; width: 218px; height: 132px; }
  .card-front .brand { left: 8px; top: 44px; }
  .card-front .brand__dot { width: 9px; height: 9px; margin-top: 4px; }
  .card-front .brand__name { font-size: 19px; }
  .card-front .brand__tagline { font-size: 4.5px; }
  .card-front .person { position: absolute; right: 12px; top: 8px; text-align: right; }
  .card-front .person__name { font-size: 8px; font-weight: 700; }
  .card-front .person__title { font-size: 5px; color: var(--ink-soft); }
  .card-front .contact { left: 118px; top: 44px; font-size: 4.5px; }

  /* envelope back */
  .envelope-back { left: 720px; top: 230px; width: 461px; height: 74px; }
  .envelope-back svg { position: absolute; inset: 0; }

  /* envelope front / compliment */
  .envelope-front { left: 667px; top: 336px; width: 514px; height: 180px; }
  .envelope-front .brand { left: 16px; top: 22px; }
  .envelope-front .brand__dot { width: 13px; height: 13px; margin-top: 6px; }
  .envelope-front .brand__name { font-size: 25px; }
  .envelope-front .brand__tagline { font-size: 5.5px; }
  .envelope-front .web { right: 18px; top: 17px; font-size: 6.5px; }
  .envelope-front .contact { left: 16px; top: 118px; font-size: 5.5px; }
</style>
</head>
<body>

  <section class="sheet letterhead" aria-label="Letterhead">
    <div class="brand">
      <span class="brand__dot"></span>
      <div>
        <div class="brand__name">Hidden<br>Meadows</div>
        <div class="brand__tagline">designing gardens for everyone</div>
      </div>
    </div>
    <p class="web">www.hddnmdws.com</p>
    <div class="contact">
      <p>P: 01632 960 418</p>
      <p>F: 01632 960 419</p>
      <p>E: emre@hddnmdws.com</p>
      <p>&nbsp;</p>
      <p>47 Foxglove Road, Ilford, Essex, RM4 8TN &nbsp; Vat No: 472 8610 35</p>
    </div>
  </section>

  <section class="sheet card-back" aria-label="Business card back">
    <div class="brand">
      <span class="brand__dot"></span>
      <div>
        <div class="brand__name">Hidden<br>Meadows</div>
        <div class="brand__tagline">designing gardens for everyone</div>
      </div>
    </div>
    <p class="web">www.hddnmdws.com</p>
  </section>

  <section class="sheet card-front" aria-label="Business card front">
    <div class="person">
      <p class="person__name">Emre Karabulut</p>
      <p class="person__title">Mr</p>
    </div>
    <div class="brand">
      <span class="brand__dot"></span>
      <div>
        <div class="brand__name">Hidden<br>Meadows</div>
        <div class="brand__tagline">designing gardens for everyone</div>
      </div>
    </div>
    <div class="contact">
      <p>P: 01632 960 418</p>
      <p>F: 01632 960 419</p>
      <p>&nbsp;</p>
      <p>47 Foxglove Road,</p>
      <p>Ilford, Essex, RM4 8TN</p>
      <p>emre@hddnmdws.com</p>
    </div>
  </section>

  <section class="sheet envelope-back" aria-label="Envelope back">
    <svg width="461" height="74" viewBox="0 0 461 74">
      <polyline points="0,2 170,52 291,52 461,2" fill="none" stroke="#bdbdbd" stroke-width="1"/>
    </svg>
  </section>

  <section class="sheet envelope-front" aria-label="Envelope front">
    <div class="brand">
      <span class="brand__dot"></span>
      <div>
        <div class="brand__name">Hidden<br>Meadows</div>
        <div class="brand__tagline">designing gardens for everyone</div>
      </div>
    </div>
    <p class="web">www.hddnmdws.com</p>
    <div class="contact">
      <p>P: 01632 960 418</p>
      <p>F: 01632 960 419</p>
      <p>E: emre@hddnmdws.com</p>
      <p>&nbsp;</p>
      <p>47 Foxglove Road, Ilford, Essex, RM4 8TN</p>
    </div>
  </section>

</body>
</html>
```